Concrete Construction Business Card design

We are a commercial concrete construction company based in Texas. a family owned business which our trade was passed down and taught by our grandfather whom we want represented in this design. our grandfathers nick name was "paprika" so we are wanting the letter G to be symbolized in some way with a red paprika . colors should be possibly a grey color back ground , green letter g and red paprika pepper , to be left for you to decide with integrity , concrete professionalism,and mexican heritage

Target Market(s)

general contractors, architects,inverstors, and engineers

Industry/Entity Type

Concrete

Contact Information for Business Card

Varela Concrete Construction LLC, Dwight Varela, 1718 Briarcliff Dr. Denton, TX 76209, (940)412-3759, dvslabworks58@mailbrook.net

```html
<!DOCTYPE html>
<html lang="en">
<head>
<meta charset="utf-8">
<title>Varela Concrete Construction LLC – Business Card</title>
<link rel="stylesheet" href="https://fonts.googleapis.com/css2?family=EB+Garamond:wght@400;500&display=swap">
<style>
  :root {
    --page: #ecebe8;
    --card-light: #d9d9d9;
    --card-mid: #b4b4b4;
    --card-dark: #8e8e8e;
    --ink: #3a3a3a;
    --ink-soft: #4a4a4a;
    --brand-green: #2e8b5a;
    --flag-green: #1f8a4c;
    --flag-white: #ffffff;
    --flag-red: #d7262b;
  }
  * { box-sizing: border-box; margin: 0; padding: 0; }
  html, body {
    width: 1200px; height: 900px; overflow: hidden;
    background: var(--page);
  }
  body {
    position: relative;
    font-family: "EB Garamond", Georgia, serif;
    color: var(--ink);
  }
  .card {
    position: absolute;
    width: 525px; height: 300px;
    background: linear-gradient(160deg, var(--card-light) 0%, var(--card-mid) 55%, var(--card-dark) 100%);
    box-shadow: 0 6px 18px rgba(0,0,0,.18);
    overflow: hidden;
  }
  .card--front { left: 60px; top: 140px; }
  .card--back  { left: 615px; top: 460px; }

  .flag-stripe {
    position: absolute; top: 0; bottom: 0;
    display: flex; width: 18px;
  }
  .flag-stripe span { flex: 1; }
  .card--front .flag-stripe { left: 16px; }
  .card--back .flag-stripe { right: 16px; }
  .flag-green { background: var(--flag-green); }
  .flag-white { background: var(--flag-white); }
  .flag-red { background: var(--flag-red); }

  /* front */
  .brand-mark {
    position: absolute; left: 0; right: 0; top: 70px;
    text-align: center;
    font-size: 64px; font-weight: 400;
    color: var(--brand-green);
    letter-spacing: 1px;
  }
  .company-name {
    position: absolute; left: 60px; right: 30px; top: 175px;
    text-align: center;
    font-size: 21px; letter-spacing: 1.5px; text-transform: uppercase;
    color: var(--ink);
  }

  /* back */
  .back-mark {
    position: absolute; left: 40px; top: 130px;
    font-size: 56px; color: var(--brand-green);
  }
  .person-name {
    position: absolute; right: 52px; top: 40px;
    font-size: 26px; font-weight: 500; letter-spacing: 1.5px;
    text-transform: uppercase; color: var(--ink-soft);
  }
  .contact-list {
    position: absolute; right: 52px; top: 92px;
    list-style: none; text-align: right;
    font-size: 15px; line-height: 28px; color: var(--ink);
  }
  .contact-list li { display: flex; justify-content: flex-end; align-items: center; gap: 10px; }
  .contact-icon { width: 16px; height: 16px; }
</style>
</head>
<body>
  <section class="card card--front" aria-label="Card front">
    <div class="flag-stripe"><span class="flag-green"></span><span class="flag-white"></span><span class="flag-red"></span></div>
    <div class="brand-mark">Varela</div>
    <p class="company-name">Varela Concrete Construction LLC</p>
  </section>

  <section class="card card--back" aria-label="Card back">
    <div class="flag-stripe"><span class="flag-red"></span><span class="flag-white"></span><span class="flag-green"></span></div>
    <div class="back-mark">Varela</div>
    <h1 class="person-name">Dwight Varela</h1>
    <ul class="contact-list">
      <li>(940)412-3759
        <svg class="contact-icon" viewBox="0 0 16 16" aria-hidden="true"><circle cx="8" cy="8" r="8" fill="#fff"/><path d="M5 4.5l1.5-.5 1 2-1 .8a5 5 0 002.7 2.7l.8-1 2 1-.5 1.5c-3 .5-7-3.5-6.5-6.5z" fill="#555"/></svg>
      </li>
      <li>dvslabworks58@mailbrook.net
        <svg class="contact-icon" viewBox="0 0 16 16" aria-hidden="true"><circle cx="8" cy="8" r="8" fill="#fff"/><rect x="4" y="5" width="8" height="6" fill="none" stroke="#555"/><path d="M4 5l4 3.5L12 5" fill="none" stroke="#555"/></svg>
      </li>
      <li>1718 Briarcliff Dr. Denton, TX 76209
        <svg class="contact-icon" viewBox="0 0 16 16" aria-hidden="true"><circle cx="8" cy="8" r="8" fill="#fff"/><path d="M8 12.5s-3-3.3-3-5.5a3 3 0 016 0c0 2.2-3 5.5-3 5.5z" fill="#555"/><circle cx="8" cy="7" r="1" fill="#fff"/></svg>
      </li>
    </ul>
  </section>
</body>
</html>
```